We need a business card design for a new company based in
Perth, Western Australia called Oveko Tiling Services. We specialize in laying Wall and Floor Tiles and Stone. We expertise in all small to large format tiles and do good quality work. Sincerity and Convition is what seperates us from others.

```html
<!DOCTYPE html>
<html lang="en">
<head>
<meta charset="utf-8">
<title>Oveko Tiling Services – Business Card</title>
<link rel="stylesheet" href="https://fonts.googleapis.com/css2?family=Source+Sans+3:wght@300;400&display=swap">
<style>
  :root {
    --page: #e4e4e6;
    --card-black: #050505;
    --grid-dark: #3a3a3a;
    --green: #8cc63f;
    --green-soft: rgba(140, 198, 63, 0);
    --steel-light: #f4f4f4;
    --steel-mid: #b9b9bb;
    --steel-dark: #5c5c5e;
    --ink: #111111;
    --white: #ffffff;
    --muted: #d8d8d8;
  }
  * { box-sizing: border-box; margin: 0; padding: 0; }
  html, body {
    width: 916px;
    height: 1200px;
    overflow: hidden;
    background: var(--page);
    font-family: "Source Sans 3", sans-serif;
  }
  .sheet {
    position: relative;
    width: 916px;
    height: 1200px;
  }
  .card {
    position: absolute;
    left: 78px;
    width: 760px;
    height: 434px;
    overflow: hidden;
    box-shadow: 0 10px 30px rgba(0, 0, 0, 0.18);
  }
  .card--front { top: 120px; background: var(--card-black); }
  .card--back  { top: 646px; background: var(--steel-mid); }
  .card__art { position: absolute; inset: 0; width: 100%; height: 100%; }

  .brand {
    position: absolute;
    display: flex;
    align-items: center;
    gap: 16px;
    font-weight: 300;
    white-space: nowrap;
  }
  .brand__square { width: 26px; height: 26px; }
  .card--front .brand { left: 150px; top: 300px; font-size: 40px; color: var(--white); }
  .card--front .brand__square { background: var(--white); }
  .card--back .brand { left: 120px; top: 176px; font-size: 52px; color: var(--ink); }
  .card--back .brand__square { background: var(--ink); width: 32px; height: 32px; }

  .contact {
    position: absolute;
    right: 48px;
    top: 44px;
    font-size: 19px;
    line-height: 1.25;
    font-weight: 300;
    color: var(--muted);
  }
  .contact__name { color: var(--white); font-size: 21px; }
  .contact__web { color: var(--green); }

  .about {
    position: absolute;
    left: 170px;
    top: 256px;
    font-size: 15.5px;
    line-height: 1.3;
    color: var(--ink);
  }
</style>
</head>
<body>
<main class="sheet">

  <section class="card card--front" aria-label="Business card front">
    <svg class="card__art" viewBox="0 0 760 434" aria-hidden="true">
      <g stroke="var(--grid-dark)" stroke-width="1" fill="none">
        <line x1="-200" y1="434" x2="234" y2="0"/>
        <line x1="0" y1="434" x2="434" y2="0"/>
        <line x1="200" y1="434" x2="634" y2="0"/>
        <line x1="400" y1="434" x2="834" y2="0"/>
        <line x1="-100" y1="0" x2="334" y2="434"/>
        <line x1="100" y1="0" x2="534" y2="434"/>
        <line x1="300" y1="0" x2="734" y2="434"/>
        <line x1="500" y1="0" x2="934" y2="434"/>
      </g>
      <polygon points="0,250 0,434 190,434" fill="var(--green)"/>
      <polygon points="190,434 330,300 420,434" fill="#8e8e90"/>
    </svg>
    <div class="brand"><span class="brand__square"></span>Oveko Tiling Services</div>
    <div class="contact">
      <div class="contact__name">Dane Harlow</div>
      <div>Phone 400 182 3XX</div>
      <div>E-mail info@ovekotiling.com</div>
      <div class="contact__web">www.ovekotiling.com</div>
    </div>
  </section>

  <section class="card card--back" aria-label="Business card back">
    <svg class="card__art" viewBox="0 0 760 434" aria-hidden="true">
      <defs>
        <linearGradient id="steel" x1="0" y1="1" x2="1" y2="0">
          <stop offset="0" stop-color="var(--steel-light)"/>
          <stop offset="0.45" stop-color="var(--steel-mid)"/>
          <stop offset="1" stop-color="var(--steel-dark)"/>
        </linearGradient>
        <linearGradient id="leaf" x1="0" y1="1" x2="0.7" y2="0.3">
          <stop offset="0" stop-color="var(--green)"/>
          <stop offset="0.55" stop-color="#b4d58a"/>
          <stop offset="1" stop-color="var(--green-soft)"/>
        </linearGradient>
      </defs>
      <rect width="760" height="434" fill="url(#steel)"/>
      <g stroke="rgba(255,255,255,0.45)" stroke-width="1" fill="none">
        <line x1="0" y1="120" x2="760" y2="120"/>
        <line x1="0" y1="250" x2="760" y2="250"/>
        <line x1="220" y1="0" x2="220" y2="434"/>
        <line x1="460" y1="0" x2="460" y2="434"/>
        <line x1="220" y1="120" x2="460" y2="0"/>
        <line x1="460" y1="120" x2="700" y2="0"/>
        <line x1="220" y1="250" x2="460" y2="120"/>
        <line x1="460" y1="250" x2="760" y2="90"/>
      </g>
      <polygon points="0,160 520,434 0,434" fill="url(#leaf)"/>
      <polygon points="0,434 0,160 200,150 760,434" fill="url(#leaf)" opacity="0.55"/>
    </svg>
    <div class="brand"><span class="brand__square"></span>Oveko Tiling Services</div>
    <p class="about">
      We specialize in laying Wall and Floor Tiles and Stone.<br>
      We are experts in all small to large format tiles and do good quality work.<br>
      Sincerity and Conviction is what seperates us from others.
    </p>
  </section>

</main>
</body>
</html>
```